Crimson Vantage Cleaning Solutions

Need a logo and business card design. I want to use a translucent business card. I want to abbreviate the name C.V.C.S. Commercial Cleaning, because my is Dov. I’d also like to incorporate a knight or something like that. I want the idea to tie in with the word Crimson. New ideas are welcome, i don’t want to limit anyone’s creativity.

Target Market(s)

Commercial Cleaning for businesses.

Contact Information for Business Card

Crimson
Vantage
Cleaning
Solutions

```html
<!DOCTYPE html>
<html lang="en">
<head>
<meta charset="utf-8">
<title>Crimson Vantage Cleaning Solutions – Business Card</title>
<link rel="stylesheet" href="https://fonts.googleapis.com/css2?family=Didact+Gothic&display=swap">
<style>
  :root {
    --stage: #ece8e1;
    --card-light: #ffffff;
    --card-dark: #0e1f27;
    --brand-blue: #2ba7d6;
    --ink: #1f2f38;
    --ink-soft: #3c4a52;
    --on-dark: #2ba7d6;
  }
  * { margin: 0; padding: 0; box-sizing: border-box; }
  html, body {
    width: 1200px; height: 942px; overflow: hidden;
    background: var(--stage);
    font-family: "Didact Gothic", "Century Gothic", sans-serif;
  }
  .stage {
    width: 1200px; height: 942px;
    display: flex; flex-direction: column;
    align-items: center; justify-content: center; gap: 48px;
  }
  .card {
    width: 580px; height: 332px;
    border-radius: 4px;
    box-shadow: 0 6px 18px rgba(0,0,0,0.14);
    position: relative;
  }
  .card--front { background: var(--card-light); display: flex; align-items: center; }
  .card--back { background: var(--card-dark); display: flex; align-items: center; justify-content: center; }

  .wordmark { display: flex; align-items: center; gap: 12px; }
  .wordmark__square { width: 22px; height: 22px; background: var(--brand-blue); flex: none; }
  .wordmark__name {
    color: var(--brand-blue);
    font-size: 19px; line-height: 1.25;
    letter-spacing: 0.08em; text-transform: uppercase;
  }
  .card--back .wordmark__name { font-size: 24px; }
  .card--back .wordmark__square { width: 28px; height: 28px; }

  .front__brand { width: 290px; padding-left: 44px; }
  .front__divider { width: 2px; height: 190px; background: var(--brand-blue); }
  .front__contact { padding-left: 34px; color: var(--ink); }
  .contact__name { font-size: 30px; color: var(--ink); line-height: 1.1; }
  .contact__title { font-size: 17px; color: var(--brand-blue); margin: 4px 0 20px; }
  .contact__list { list-style: none; font-size: 16px; color: var(--ink-soft); }
  .contact__list li { display: flex; align-items: center; gap: 10px; margin-bottom: 7px; }
  .contact__icon { width: 15px; height: 15px; flex: none; }
</style>
</head>
<body>
<main class="stage">
  <section class="card card--front" aria-label="Business card front">
    <div class="front__brand">
      <div class="wordmark">
        <span class="wordmark__square"></span>
        <span class="wordmark__name">Crimson Vantage<br>Cleaning Solutions</span>
      </div>
    </div>
    <div class="front__divider"></div>
    <div class="front__contact">
      <p class="contact__name">Your Name</p>
      <p class="contact__title">Job Title</p>
      <ul class="contact__list">
        <li>
          <svg class="contact__icon" viewBox="0 0 16 16"><rect width="16" height="16" rx="3" fill="#2ba7d6"/><path d="M5 4h2l1 2.5-1.3 1a6 6 0 0 0 2.8 2.8l1-1.3L13 10v2a1 1 0 0 1-1 1A9 9 0 0 1 4 5a1 1 0 0 1 1-1z" fill="#fff"/></svg>
          000 000 0000
        </li>
        <li>
          <svg class="contact__icon" viewBox="0 0 16 16"><rect width="16" height="16" rx="3" fill="#2ba7d6"/><rect x="3" y="4.5" width="10" height="7" fill="none" stroke="#fff" stroke-width="1.2"/><path d="M3 4.5l5 4 5-4" fill="none" stroke="#fff" stroke-width="1.2"/></svg>
          youremail@xyz.com
        </li>
        <li>
          <svg class="contact__icon" viewBox="0 0 16 16"><circle cx="8" cy="8" r="7" fill="none" stroke="#2ba7d6" stroke-width="1.3"/><ellipse cx="8" cy="8" rx="3" ry="7" fill="none" stroke="#2ba7d6" stroke-width="1.1"/><path d="M1 8h14" stroke="#2ba7d6" stroke-width="1.1"/></svg>
          www.yourwebsite.com
        </li>
      </ul>
    </div>
  </section>

  <section class="card card--back" aria-label="Business card back">
    <div class="wordmark">
      <span class="wordmark__square"></span>
      <span class="wordmark__name">Crimson Vantage<br>Cleaning Solutions</span>
    </div>
  </section>
</main>
</body>
</html>
```